Brindle's Coating & Renewal Letterhead Design We want to revamp out old traditional letterhead with the new logo designs that are attached. We are working on getting all our company items from vehicles, business, cards, t-shirts, letterhead to match. This should include company colors, fonts, and flow of items that we have attached below.

Industry/Entity Type

Construction Company

Font styles to use
Sans Serif
Other font styles liked:
• Bold with outline

Colors
ec1f27
ffffff

Requirements
Must have
• Company Name: Brindle's Coating & Renewal
• Address: 4172 SW 83rd Ter Harrow Cove fl 30418
• Office Number: (555) 240-6193
• Email: brindlesrenewal@mailnest-example.com
• License Number: QRT8046392
Nice to have
• Company Colors: red, white, black, and grey

```html
<!DOCTYPE html>
<html lang="en">
<head>
<meta charset="utf-8">
<title>Brindle's Coating &amp; Renewal Letterhead</title>
<link rel="stylesheet" href="https://fonts.googleapis.com/css2?family=Montserrat:wght@400;500;600;700&display=swap">
<style>
  :root {
    --brand-red: #ec1f27;
    --accent-orange: #f04e23;
    --ink: #333333;
    --body-ink: #3a3a3a;
    --swoosh-grey: #e6e6e6;
    --texture-grey: #f5f5f5;
    --blush: #f9d3c8;
    --paper: #ffffff;
    --backdrop: #f0f0f0;
  }
  * { box-sizing: border-box; margin: 0; padding: 0; }
  html, body {
    width: 894px; height: 1200px; overflow: hidden;
    background: var(--backdrop);
    font-family: "Montserrat", sans-serif;
  }
  .letterhead {
    position: absolute; left: 22px; top: 0;
    width: 849px; height: 1200px;
    background: var(--paper);
    overflow: hidden;
  }
  .decor { position: absolute; inset: 0; width: 849px; height: 1200px; }
  .brand {
    position: absolute; left: 60px; top: 58px;
    display: flex; align-items: center; gap: 12px;
    color: var(--accent-orange); font-weight: 700;
  }
  .brand-mark { width: 18px; height: 18px; background: var(--accent-orange); }
  .brand-name { font-size: 30px; line-height: 1.05; letter-spacing: 0.5px; }
  .brand-name span { display: block; font-size: 19px; letter-spacing: 1.2px; }
  .contact {
    position: absolute; right: 63px; top: 50px;
    list-style: none; text-align: right;
    font-weight: 700; font-size: 15px; color: var(--ink);
  }
  .contact li { display: flex; justify-content: flex-end; align-items: center; gap: 10px; height: 21px; }
  .contact-icon {
    width: 17px; height: 17px; border: 1.3px solid var(--accent-orange);
    border-radius: 50%; display: inline-flex; align-items: center; justify-content: center;
  }
  .header-rule { position: absolute; left: 354px; right: 0; top: 136px; height: 2px; background: var(--brand-red); }
  .signoff { position: absolute; left: 60px; top: 238px; color: var(--ink); }
  .signoff-closing { font-size: 13px; font-weight: 400; }
  .signoff-name { margin-top: 14px; font-size: 22px; font-weight: 700; letter-spacing: 0.5px; line-height: 1; }
  .signoff-title { margin-top: 5px; font-size: 15px; font-weight: 700; }
  .letter-body {
    position: absolute; left: 60px; top: 459px; width: 735px;
    font-size: 13.4px; line-height: 28px; color: var(--body-ink); font-weight: 400;
  }
  .letter-body p + p { margin-top: 28px; }
  .letter-body p.spaced { margin-top: 56px; }
  .footer-rule { position: absolute; left: 0; right: 0; top: 1143px; height: 2px; background: var(--brand-red); }
  .footer {
    position: absolute; left: 60px; right: 64px; top: 1161px;
    display: flex; justify-content: space-between;
    font-size: 16px; font-weight: 700; color: var(--ink);
  }
  .license { color: var(--brand-red); }
</style>
</head>
<body>
<main class="letterhead">
  <svg class="decor" viewBox="0 0 849 1200" aria-hidden="true">
    <path d="M0 340 C 250 360, 560 300, 849 160 L 849 865 C 560 930, 250 990, 0 1035 Z" fill="var(--texture-grey)"/>
    <path d="M0 271 C 330 240, 580 150, 731 0 L 805 0 C 620 170, 360 265, 0 281 Z" fill="var(--swoosh-grey)"/>
    <path d="M505 212 C 640 170, 760 110, 849 29 L 849 70 C 760 130, 640 185, 505 212 Z" fill="var(--swoosh-grey)"/>
    <path d="M195 1200 C 300 1160, 400 1125, 498 1103 C 420 1130, 330 1170, 270 1200 Z" fill="var(--blush)"/>
    <path d="M498 1200 C 620 1160, 740 1125, 846 1103 C 760 1130, 660 1170, 575 1200 Z" fill="var(--blush)"/>
  </svg>
  <svg class="decor" viewBox="0 0 849 1200" role="img" aria-label="Faint dotted halftone texture across the letter area">
    <rect x="0" y="0" width="0" height="0" fill="none"/>
  </svg>

  <div class="brand">
    <span class="brand-mark"></span>
    <div class="brand-name">BRINDLE'S<span>COATING &amp; RENEWAL</span></div>
  </div>

  <ul class="contact">
    <li>(555) 240-6193
      <span class="contact-icon"><svg width="9" height="9" viewBox="0 0 10 10"><path d="M2 1 L4 1 L4.6 3 L3.5 4 C4 5.2 4.8 6 6 6.5 L7 5.4 L9 6 L9 8 C5 8.5 1.5 5 2 1 Z" fill="var(--accent-orange)"/></svg></span>
    </li>
    <li>brindlesrenewal@mailnest-example.com
      <span class="contact-icon"><svg width="9" height="7" viewBox="0 0 10 7"><rect x="0.5" y="0.5" width="9" height="6" fill="none" stroke="var(--accent-orange)"/><path d="M0.5 0.5 L5 4 L9.5 0.5" fill="none" stroke="var(--accent-orange)"/></svg></span>
    </li>
    <li>www.brindlesrenewal-example.com
      <span class="contact-icon"><svg width="10" height="10" viewBox="0 0 10 10"><circle cx="5" cy="5" r="4.3" fill="none" stroke="var(--accent-orange)"/><ellipse cx="5" cy="5" rx="2" ry="4.3" fill="none" stroke="var(--accent-orange)"/><path d="M0.7 5 H9.3" stroke="var(--accent-orange)"/></svg></span>
    </li>
  </ul>
  <div class="header-rule"></div>

  <section class="signoff">
    <p class="signoff-closing">Sincearly,</p>
    <p class="signoff-name">MARCUS HALE</p>
    <p class="signoff-title">Director</p>
  </section>

  <article class="letter-body">
    <p>This is a sample letter that has been placed to demonstrate typing remat (Your Company).letterhead design. When positioned properly, it will serve to work in harmony with all other elements letterhead. This letterhead design is meant to project an image&nbsp; This letterhead design is meant project an image of professionalism reliability. By using simple aligen we have created a very spacious feeling. The simplicity suggest&nbsp; rengththe spaciousnes contributes haesthetics the layout. These basic qualities along with the (Your Company)</p>
    <p>look and helps reinforce the (Your Company) brand. letterhead design is meant to project an image design. When positioned properly, it will serve to work in harmony all the other elements letterhead. sionalism and reliability.</p>
    <p class="spaced">This letterhead design is based on the (Form of your logo) form (Your Company) logo. Each stationery we have created a very spacious feeling. The simplicity suggests strength the spaciousnes contribute part of the (Form of your logo). This letterhead design is based on the (Form of your logo) form (Your Company) logo. Each stationery we have created a very spacious feeling. The simplicity suggests strength the spaciousnes contribute part of the (Form of your logo).</p>
  </article>

  <div class="footer-rule"></div>
  <footer class="footer">
    <span class="address">4172 SW 83rd Ter . Harrow Cove, Florida 30418</span>
    <span class="license">QRT8046392</span>
  </footer>
</main>
</body>
</html>
```